We are a organisation that provide outdoor adventure based tours to international students in New Ze

We are a Waikato New Zealand based company that runs adventure and outdoor tours around New Zealand. Activities included in our tours are mountain biking, rafting, sea kayaking, surfing/SUPing, luge, high ropes course, tramping, snorkelling and cultural activities. We need a Name/Logo, advertisement and information Flyers that we can give to the students/customers ASAP. We still haven't come up with a name so are hoping that designers can be more creative than we are. we are running our fist trip Dec 15th-22nd 2013.

Attached are some bits of information that we need to be included in the flyer. We need to get the 'Brightwater Tour' filled up first and the 'Kerrin's Shell Tour' will be later.

We want it to be an exciting and edgy design with an 'outdoor' feel to it. There is the potential for this design to be expanded into our website.

The brochure/ Flyer can come in any creative format.

Target Market(s)

High school aged students. We will be expanding to University students in the future. We also need to make sure that this is appealing to the parents. It will be them who will agree to them going on the trips after all.

Industry/Entity Type

It Company

Requirements
Must have
• Our Contact details.
Booking Info
Tour information from attached.
Nice to have
• Photos can use the ones we have put into the attachment or other images from the outdoors that designers can source to make it look good.

```html
<!DOCTYPE html>
<html lang="en">
<head>
<meta charset="utf-8">
<title>Brightwater Tour – Adventure and outdoor tours around New Zealand</title>
<link rel="stylesheet" href="https://fonts.googleapis.com/css2?family=Roboto+Condensed:wght@400;700&family=Source+Sans+3:wght@400;600&display=swap">
<style>
  :root {
    --page-bg: #e9e4dc;
    --sea-deep: #1260b0;
    --sea-mid: #1f7ccc;
    --sea-light: #3aa2e4;
    --wave-pale: #bfe2f8;
    --white: #ffffff;
    --navy: #1d3f8f;
    --red: #e3262b;
    --yellow: #f4e81c;
    --ink: #3a3a3a;
  }
  * { margin: 0; padding: 0; box-sizing: border-box; }
  html, body { width: 921px; height: 1200px; overflow: hidden; background: var(--page-bg); }
  .flyer {
    position: absolute; left: 36px; top: 7px; width: 848px; height: 1186px;
    background: linear-gradient(180deg, var(--sea-deep) 0%, var(--sea-mid) 45%, var(--sea-light) 80%);
    overflow: hidden; font-family: "Source Sans 3", sans-serif; color: var(--white);
    box-shadow: 0 4px 14px rgba(0,0,0,.25);
  }
  .abs { position: absolute; }
  .headline {
    top: 26px; left: 0; width: 100%; text-align: center;
    font-family: "Roboto Condensed", sans-serif; font-weight: 700; font-size: 34px;
  }
  .hero-photo {
    top: 110px; left: 0; width: 848px; height: 370px;
    background: linear-gradient(180deg, #c8def0 0%, #a9c7de 28%, #5f7f72 42%, #7c97a8 55%, #3f4a4e 72%, #5a5b55 100%);
  }
  .waves { top: 0; left: 0; width: 848px; height: 1186px; pointer-events: none; }
  .tour-name {
    top: 128px; left: 105px; font-family: "Roboto Condensed", sans-serif; font-weight: 700;
    font-size: 70px; color: var(--red); letter-spacing: -0.5px;
  }
  .tagline {
    top: 470px; left: 90px; font-family: "Roboto Condensed", sans-serif; font-weight: 700;
    font-size: 44px; color: var(--navy);
  }
  .promise {
    top: 578px; left: 37px; font-family: "Roboto Condensed", sans-serif; font-weight: 700;
    font-size: 22px; line-height: 31px; color: var(--yellow);
  }
  .hooks {
    top: 530px; left: 612px; list-style: none; font-family: "Roboto Condensed", sans-serif;
    font-weight: 700; font-size: 19px; line-height: 24px;
  }
  .hooks li { padding-left: 28px; position: relative; margin-bottom: 6px; }
  .hooks li::before { content: "☛"; position: absolute; left: 0; top: 0; }
  .hooks .sub { display: block; }
  .platform { top: 665px; left: 35px; font-size: 23px; line-height: 28px; }
  .goals { top: 743px; left: 35px; width: 290px; font-size: 16px; line-height: 27px; list-style: none; }
  .goals li { display: flex; }
  .goals .num { width: 22px; flex: none; }
  .goals .wrap { line-height: 20px; padding-top: 3px; }
  .extra { top: 875px; left: 35px; width: 275px; font-size: 16px; line-height: 20px; }
  .scene-photo {
    top: 676px; left: 340px; width: 380px; height: 280px; border-radius: 42%;
    background: linear-gradient(180deg, #dcebf6 0%, #9fc0d8 30%, #3f6e86 48%, #4f7a50 62%, #2f5a2c 100%);
  }
  .contact-panel { top: 990px; left: 0; width: 848px; height: 196px; background: var(--white); }
  .divider { top: 1005px; left: 275px; width: 2px; height: 165px; background: #555; }
  .contact-lead { top: 1006px; left: 50px; font-size: 20px; font-weight: 600; color: var(--red); }
  .contact-name { top: 1030px; left: 48px; font-family: "Roboto Condensed", sans-serif; font-weight: 700; font-size: 31px; color: var(--red); }
  .contact-phone { top: 1100px; left: 45px; font-family: "Roboto Condensed", sans-serif; font-weight: 700; font-size: 32px; color: var(--ink); }
  .contact-email { top: 1148px; left: 45px; font-size: 12px; letter-spacing: .3px; color: var(--ink); }
  .about { top: 1005px; left: 292px; width: 538px; font-size: 14px; line-height: 17px; color: var(--ink); text-align: justify; }
  .about p + p { margin-top: 9px; }
  .dates { top: 1134px; left: 292px; width: 540px; display: flex; align-items: baseline; color: var(--ink); }
  .dates-label { font-family: "Roboto Condensed", sans-serif; font-weight: 700; font-size: 26px; margin-right: 8px; }
  .dates-value { font-family: "Roboto Condensed", sans-serif; font-weight: 700; font-size: 31px; color: var(--red); }
  .dates-limit { margin-left: auto; font-size: 18px; font-weight: 600; letter-spacing: .5px; }
</style>
</head>
<body>
<div class="flyer">
  <div class="abs hero-photo" role="img" aria-label="Photo of a student group gathered on a lakeshore beside stacked kayaks, forested hills behind"></div>

  <svg class="abs waves" viewBox="0 0 848 1186" aria-hidden="true">
    <path d="M0 0 H848 V120 C700 70 560 175 380 150 C230 130 120 170 0 150 Z" fill="var(--sea-deep)"/>
    <path d="M0 150 C120 170 230 130 380 150 C560 175 700 70 848 120 V135 C700 90 560 190 380 168 C230 150 120 185 0 165 Z" fill="var(--white)"/>
    <path d="M0 430 C160 470 300 400 470 440 C620 475 740 420 848 430 V1186 H0 Z" fill="var(--sea-mid)"/>
    <path d="M0 430 C160 470 300 400 470 440 C620 475 740 420 848 430 V450 C740 440 620 500 470 462 C300 420 160 495 0 455 Z" fill="var(--white)"/>
    <path d="M0 470 C180 500 330 450 500 485 C660 515 760 470 848 478 V520 C720 505 600 550 440 520 C280 490 150 540 0 515 Z" fill="var(--wave-pale)" opacity=".55"/>
    <path d="M0 540 C200 560 360 520 560 560 C700 585 790 555 848 560 V640 C700 610 520 660 300 620 C160 600 70 630 0 620 Z" fill="var(--sea-light)" opacity=".45"/>
    <path d="M0 950 C200 1005 420 920 600 958 C720 982 800 958 848 952 V1186 H0 Z" fill="var(--wave-pale)" opacity=".6"/>
  </svg>

  <div class="abs headline">Adventure and outdoor tours around New Zealand</div>
  <div class="abs tour-name">Brightwater Tour</div>
  <div class="abs tagline">‘Take the path less travelled’</div>

  <div class="abs promise">We are the only adventure tour organization<br>providing exciting experiences on and off the beaten track</div>

  <ul class="abs hooks">
    <li>Love the outdoors?</li>
    <li>Want some better<span class="sub">stories about your NZ</span><span class="sub">exchange?</span></li>
    <li>Check us out!!</li>
  </ul>

  <p class="abs platform">Our tours offer a platform<br>for foreign students to …</p>
  <ol class="abs goals">
    <li><span class="num">1.</span>Build confidence</li>
    <li><span class="num">2.</span>Create positive relationships</li>
    <li><span class="num">3.</span>Experience new cultures</li>
    <li><span class="num">4.</span><span class="wrap">Solve problems in an unfamiliar and challenging outdoor environment</span></li>
  </ol>
  <p class="abs extra">Our tours have many great popular NZ tourist activities but more importantly go where no other similar tours go. We create our own path less travelled!!!</p>

  <div class="abs scene-photo" role="img" aria-label="Photo of a quiet bay with bush-covered headland and a rocky shoreline"></div>

  <div class="abs contact-panel"></div>
  <div class="abs divider"></div>
  <div class="abs contact-lead">Please free to contact;</div>
  <div class="abs contact-name">Rowan Hartley</div>
  <div class="abs contact-phone">0215550172</div>
  <div class="abs contact-email">email: rowanhartley@mailbox.co.nz</div>

  <div class="abs about">
    <p>We are all about making your story in NZ one worth telling. Here at ……….Tours we pride ourselves in providing the most memorable and exciting adventure based tours for students JUST LIKE YOU. We don’t just take you to some of New Zealand’s world-class adventure activities, we also take you deeper into the real New Zealand other tours don’t touch.</p>
    <p>Our guides are addicted to adventure and the outdoors. We are ready to have some fun and share with you our knowledge of our beautiful country. Come and get into it!</p>
  </div>
  <div class="abs dates">
    <span class="dates-label">Tour dates:</span>
    <span class="dates-value">Dec 15th -22nd</span>
    <span class="dates-limit">Limited to 30 spaces</span>
  </div>
</div>
</body>
</html>
```